Business Card

I need a business card that really pops for a potential customer or person who refers a personal injury lead. I want to highlight our office locations, but only address that needs to be on the card is my office's main address. I want a sleek, modern and minimalist design.

```html
<!DOCTYPE html>
<html lang="en">
<head>
<meta charset="utf-8">
<title>Lakeshore Injury Lawyers – Business Card</title>
<link rel="stylesheet" href="https://fonts.googleapis.com/css2?family=Jost:wght@400;500;700&display=swap">
<style>
  :root {
    --bg: #e4e4e4;
    --card: #f6f6f6;
    --ink: #2f2f2f;
    --muted: #7d7d7d;
    --rule: #333333;
  }
  * { margin: 0; padding: 0; box-sizing: border-box; }
  html, body { width: 1200px; height: 1200px; overflow: hidden; }
  body {
    background: var(--bg);
    font-family: "Jost", Arial, sans-serif;
    color: var(--ink);
    position: relative;
  }
  .card {
    position: absolute;
    left: 235px;
    width: 730px;
    height: 417px;
    background: var(--card);
  }
  .card--front { top: 160px; }
  .card--back { top: 632px; }

  .firm-name {
    position: absolute;
    font-size: 32px;
    font-weight: 500;
    line-height: 1.2;
    color: var(--ink);
  }
  .card--front .firm-name { left: 0; right: 0; top: 166px; text-align: center; }
  .card--back .firm-name { left: 52px; top: 72px; }

  .address {
    position: absolute;
    left: 0; right: 0; top: 296px;
    text-align: center;
    font-size: 19px;
    line-height: 29px;
  }
  .address__pin { display: block; margin: 0 auto 6px; width: 18px; height: 22px; }

  .person { position: absolute; right: 57px; top: 220px; text-align: right; }
  .person__name { font-size: 34px; font-weight: 700; line-height: 1; }
  .person__title { font-size: 19px; color: var(--muted); margin-top: 6px; }

  .divider {
    position: absolute; left: 52px; right: 57px; top: 290px;
    height: 2px; background: var(--rule);
  }

  .contact { position: absolute; top: 306px; font-size: 19px; color: var(--muted); }
  .contact--left { left: 52px; }
  .contact--right { right: 55px; text-align: right; }
  .contact__row { display: flex; align-items: center; height: 29px; gap: 12px; }
  .contact--right .contact__row { justify-content: flex-end; }
  .contact__icon { width: 17px; height: 17px; fill: var(--ink); flex: none; }
</style>
</head>
<body>
  <section class="card card--front">
    <p class="firm-name">Lakeshore Injury Lawyers</p>
    <div class="address">
      <svg class="address__pin" viewBox="0 0 18 22" aria-hidden="true">
        <path d="M9 0C4.3 0 .8 3.6.8 8.1 .8 13.6 9 22 9 22s8.2-8.4 8.2-13.9C17.2 3.6 13.7 0 9 0zm0 11.3a3.3 3.3 0 1 1 0-6.6 3.3 3.3 0 0 1 0 6.6z" fill="#2f2f2f"/>
      </svg>
      <p>480 West Harbor Avenue, Suite 1200</p>
      <p>Chicago, IL 60611</p>
    </div>
  </section>

  <section class="card card--back">
    <p class="firm-name">Lakeshore Injury Lawyers</p>
    <div class="person">
      <p class="person__name">Daniel T. Moreland</p>
      <p class="person__title">Co-Founder</p>
    </div>
    <div class="divider"></div>
    <div class="contact contact--left">
      <p class="contact__row">
        <svg class="contact__icon" viewBox="0 0 24 24" aria-hidden="true"><path d="M6.6 10.8a15.1 15.1 0 0 0 6.6 6.6l2.2-2.2c.3-.3.7-.4 1-.2 1.1.4 2.3.6 3.6.6.6 0 1 .4 1 1V20c0 .6-.4 1-1 1A17 17 0 0 1 3 4c0-.6.4-1 1-1h3.5c.6 0 1 .4 1 1 0 1.3.2 2.5.6 3.6.1.3 0 .7-.2 1z"/></svg>
        <span>312-555-0147</span>
      </p>
      <p class="contact__row">
        <svg class="contact__icon" viewBox="0 0 24 24" aria-hidden="true"><path d="M10 3C5 3 1.5 6 1.5 9.7c0 2 1 3.7 2.6 4.9L3 18l3.9-1.9c1 .3 2 .4 3.1.4 4.9 0 8.5-3 8.5-6.8S14.9 3 10 3z"/><path d="M20.3 10.5c0 4.3-4 7.6-9 7.8 1.3 1.4 3.3 2.2 5.5 2.2.8 0 1.5-.1 2.2-.3l3 1.5-.8-2.7c1.1-.9 1.8-2.2 1.8-3.6 0-1.9-1.1-3.6-2.7-4.9z"/></svg>
        <span>312-555-0192</span>
      </p>
    </div>
    <div class="contact contact--right">
      <p class="contact__row">
        <span>hello@lakeshoreinjurylaw.com</span>
        <svg class="contact__icon" viewBox="0 0 24 24" aria-hidden="true"><path d="M2 5h20v2.2l-10 6-10-6z"/><path d="M2 9.5l10 6 10-6V19H2z"/></svg>
      </p>
      <p class="contact__row">
        <span>www.lakeshoreinjurylaw</span>
        <svg class="contact__icon" viewBox="0 0 24 24" aria-hidden="true"><circle cx="12" cy="12" r="10"/><g fill="none" stroke="#f6f6f6" stroke-width="1.4"><ellipse cx="12" cy="12" rx="4.2" ry="10"/><path d="M12 2v20M2 12h20M3.5 7h17M3.5 17h17"/></g></svg>
      </p>
    </div>
  </section>
</body>
</html>
```